Etiketten für Weinbaubetrieb
Recht herzlichen Dank für die rasche Umsetzung und die punktgenaue Umsetzung von diversen Wünschen. Das Design hat uns schwer begeistert, wir hoffen dass dieses genauso gut ankommt bei unseren Kunden wie bei uns.
Zielgruppe
Weinbaubetrieb
Aufgabenstellung
Wollen ein neues Flaschen-Etikett für unsere Wein Magnumflaschen kreieren (Limitierte Stückzahl), Hintergrund soll Schwarz sein, Stil: Schlicht und Edel, ca 9,5 x 9,5 cm / Schwarz/weiß max. silber und Gold (Logo muss nicht unbedingt ersichtlich sein)
Bezeichnung: quiet harbor;
limited edion weingut brandt
Angefügt sind unsere bisherige Etikette weißwein: DAC.jpg u. Rotwein: roesler.jpg
bzw. in welche Richtung es gehen soll: Magnnum.pdf

```html
<!DOCTYPE html>
<html lang="de">
<head>
<meta charset="utf-8">
<title>quiet harbor – Etikett Magnum Limited Edition</title>
<link rel="stylesheet" href="https://fonts.googleapis.com/css2?family=Bodoni+Moda:opsz,wght@6..96,500&family=Ephesis&display=swap">
<style>
  :root {
    --page: #232325;
    --label: #0a0b0f;
    --gold-light: #d6a866;
    --gold: #b8843f;
    --gold-deep: #8a5a26;
  }
  * { margin: 0; padding: 0; box-sizing: border-box; }
  html, body {
    width: 1200px;
    height: 1200px;
    overflow: hidden;
    background: var(--page);
  }
  .label {
    position: absolute;
    left: 170px;
    top: 170px;
    width: 860px;
    height: 860px;
    background: var(--label);
  }
  .gold {
    color: var(--gold);
    background: linear-gradient(160deg, var(--gold-light) 0%, var(--gold) 45%, var(--gold-deep) 100%);
    -webkit-background-clip: text;
    background-clip: text;
    -webkit-text-fill-color: transparent;
  }
  .wordmark {
    position: absolute;
    left: 118px;
    top: 40px;
    font-family: "Bodoni Moda", "Didot", serif;
    font-weight: 500;
    font-size: 270px;
    line-height: 1;
    letter-spacing: -8px;
  }
  .subtitle {
    position: absolute;
    left: 130px;
    top: 380px;
    font-family: "Ephesis", cursive;
    font-size: 84px;
    line-height: 1;
  }
  .edition {
    position: absolute;
    left: 130px;
    top: 590px;
    font-family: "Ephesis", cursive;
    font-size: 92px;
    line-height: 0.82;
  }
  .edition span { display: block; }
</style>
</head>
<body>
  <main class="label">
    <h1 class="wordmark gold">quiet</h1>
    <p class="subtitle gold">harbor</p>
    <p class="edition gold">
      <span>limited edition</span>
      <span>weingut brandt</span>
    </p>
  </main>
</body>
</html>
```